Home Baker of cakes, muffins, cookies and pastries.

I am looking for business cards for my home baking business called " Zippy Pom-Pom Bakes " - I want them to be super cute and girly, yet simple and modern at the same time. Pastel colours is what I envision with the main colour being baby pink.

```html
<!DOCTYPE html>
<html lang="en">
<head>
<meta charset="utf-8">
<title>Zippy Pom-Pom Bakes – Business Cards</title>
<link rel="stylesheet" href="https://fonts.googleapis.com/css2?family=Dancing+Script:wght@500&family=Arimo:wght@400&display=swap">
<style>
  :root {
    --backdrop: #3b3b3d;
    --baby-pink: #ec8ba6;
    --deep-pink: #d66f8c;
    --teal: #7cc3c8;
    --paper: #ffffff;
    --paper-shade: #eeeeee;
    --ink-grey: #5d5d5d;
    --name-pink: #c95e80;
  }
  html, body {
    margin: 0;
    padding: 0;
    width: 1200px;
    height: 997px;
    overflow: hidden;
    background: var(--backdrop);
  }
  .sheet {
    position: relative;
    width: 1200px;
    height: 997px;
    display: flex;
    align-items: center;
    justify-content: center;
    gap: 60px;
  }
  .card {
    position: relative;
    width: 520px;
    height: 300px;
    border-radius: 20px;
    overflow: hidden;
    box-shadow: 0 18px 40px rgba(0,0,0,0.45);
    font-family: "Arimo", Arial, sans-serif;
  }
  /* back side */
  .card--back {
    background: linear-gradient(160deg, #f197b0 0%, var(--baby-pink) 60%, #e57f9d 100%);
  }
  .card--back .brand {
    position: absolute;
    top: 105px;
    left: 0;
    right: 0;
    text-align: center;
    color: var(--paper);
  }
  .card--back .website {
    position: absolute;
    top: 200px;
    left: 0;
    right: 0;
    text-align: center;
    color: var(--paper);
    font-size: 14px;
    font-weight: 700;
    letter-spacing: 1px;
  }
  /* front side */
  .card--front {
    background: linear-gradient(180deg, var(--paper) 0%, var(--paper-shade) 100%);
  }
  .card--front .brand {
    position: absolute;
    top: 62px;
    left: 0;
    right: 0;
    text-align: center;
    color: var(--baby-pink);
  }
  .brand {
    font-family: "Dancing Script", cursive;
    font-weight: 500;
    font-size: 40px;
    line-height: 1;
  }
  .brand__dot {
    display: inline-block;
    width: 14px;
    height: 14px;
    border-radius: 50%;
    background: currentColor;
    margin-right: 10px;
    vertical-align: middle;
  }
  .card--front .brand__dot { background: var(--teal); }
  .holder {
    position: absolute;
    top: 120px;
    right: 30px;
    text-align: right;
  }
  .holder__name {
    font-family: "Dancing Script", cursive;
    font-size: 21px;
    color: var(--name-pink);
    line-height: 1;
  }
  .holder__role {
    font-size: 15px;
    color: var(--teal);
    margin-top: 2px;
  }
  .wave {
    position: absolute;
    left: 0;
    bottom: 0;
    width: 520px;
    height: 300px;
  }
  .contact {
    position: absolute;
    left: 16px;
    bottom: 22px;
    list-style: none;
    margin: 0;
    padding: 0;
    color: var(--paper);
    font-size: 13px;
    line-height: 20px;
  }
  .contact__item {
    display: flex;
    align-items: center;
    gap: 7px;
  }
  .contact__item--first { margin-left: 22px; }
  .contact__icon {
    width: 14px;
    height: 14px;
    flex: none;
  }
</style>
</head>
<body>
<main class="sheet">

  <section class="card card--back" aria-label="Business card back">
    <div class="brand"><span class="brand__dot"></span>Zippy Pom-Pom Bakes</div>
    <div class="website">www.zippypompom.com</div>
  </section>

  <section class="card card--front" aria-label="Business card front">
    <div class="brand"><span class="brand__dot"></span>Zippy Pom-Pom Bakes</div>

    <div class="holder">
      <div class="holder__name">Clara Wynn</div>
      <div class="holder__role">Chef</div>
    </div>

    <svg class="wave" viewBox="0 0 520 300" aria-hidden="true">
      <path d="M0 232 C 90 175, 260 170, 520 175 L520 300 L0 300 Z" fill="var(--deep-pink)"/>
      <path d="M0 218 C 90 168, 260 158, 520 165" fill="none" stroke="var(--teal)" stroke-width="9"/>
      <path d="M0 226 C 90 175, 260 166, 520 172" fill="none" stroke="var(--paper)" stroke-width="6"/>
    </svg>

    <ul class="contact">
      <li class="contact__item contact__item--first">07 5550 1234</li>
      <li class="contact__item">
        <svg class="contact__icon" viewBox="0 0 14 14" aria-hidden="true">
          <circle cx="7" cy="7" r="7" fill="var(--paper)"/>
          <path d="M4.5 3.5 l1.5 0 l0.6 2 l-1 0.8 a5 5 0 0 0 2.1 2.1 l0.8 -1 l2 0.6 l0 1.5 a1 1 0 0 1 -1 1 A6 6 0 0 1 3.5 4.5 a1 1 0 0 1 1 -1z" fill="var(--deep-pink)"/>
        </svg>
        clara@zippypompom.com
      </li>
      <li class="contact__item">
        <svg class="contact__icon" viewBox="0 0 14 14" aria-hidden="true">
          <circle cx="7" cy="7" r="7" fill="var(--paper)"/>
          <rect x="3.5" y="4.5" width="7" height="5" fill="none" stroke="var(--deep-pink)" stroke-width="1"/>
          <path d="M3.5 4.5 L7 7.3 L10.5 4.5" fill="none" stroke="var(--deep-pink)" stroke-width="1"/>
        </svg>
        12/40 Maple Lane, Rosewood Qld 4340
      </li>
    </ul>
  </section>

</main>
</body>
</html>
```